Business Card Design Project

We currently have existing logo. Looking to have nice colorful business cards done.
We would like the name of business, phone, address, email and website

Target Market(s)

25-50

Industry/Entity Type

Business

Requirements
Must have
• We are currently using
Samrakan font for our business name
Rage italic font for tag line..
you may visit our website at www.velmorita.com to get good feel

velmorita means colors in India. google velmorita to get more info

```html
<!DOCTYPE html>
<html lang="en">
<head>
<meta charset="UTF-8">
<title>Velmorita – Business Cards</title>
<link rel="stylesheet" href="https://fonts.googleapis.com/css2?family=Cormorant+Garamond:ital,wght@0,500;1,500&display=swap">
<style>
  :root {
    --backdrop: #2b2b2b;
    --card: #5a0a0e;
    --brand-red: #d8323a;
    --tagline: #e0702a;
    --label: #d8323a;
    --value: #f0b862;
    --mandala-core: #f3a13a;
    --mandala-mid: #d8323a;
    --mandala-edge: #7a1014;
  }
  * { margin: 0; padding: 0; box-sizing: border-box; }
  html, body { width: 1200px; height: 900px; overflow: hidden; }
  body {
    background: var(--backdrop);
    font-family: "Cormorant Garamond", Georgia, serif;
    font-variant-numeric: lining-nums;
    position: relative;
  }
  .card {
    position: absolute;
    top: 195px;
    width: 310px;
    height: 508px;
    background: var(--card);
    border-radius: 28px;
    overflow: hidden;
  }
  .card--front { left: 263px; }
  .card--back { left: 629px; }
  .brand {
    position: absolute;
    left: 32px;
    top: 44px;
    width: 252px;
  }
  .brand__name {
    font-size: 44px;
    font-weight: 500;
    line-height: 1;
    color: var(--brand-red);
    letter-spacing: 0.5px;
  }
  .brand__tagline {
    display: block;
    text-align: right;
    margin-top: 4px;
    font-size: 17px;
    font-style: italic;
    color: var(--tagline);
  }
  .mandala {
    position: absolute;
    width: 276px;
    height: 276px;
    border-radius: 50%;
    background: radial-gradient(circle, var(--mandala-core) 0%, var(--mandala-mid) 38%, #b8242a 62%, #c9a04a 66%, var(--mandala-mid) 72%, var(--mandala-edge) 100%);
  }
  .card--front .mandala { left: 17px; top: 172px; }
  .card--back .mandala { left: 17px; top: 374px; }
  .contact {
    position: absolute;
    top: 152px;
    left: 0;
    width: 100%;
    text-align: center;
    list-style: none;
  }
  .contact__item { margin-bottom: 8px; }
  .contact__label {
    display: block;
    font-size: 13px;
    color: var(--label);
    line-height: 1.25;
  }
  .contact__value {
    display: block;
    font-size: 16px;
    color: var(--value);
    line-height: 1.15;
  }
</style>
</head>
<body>
  <section class="card card--front">
    <div class="brand">
      <div class="brand__name">velmorita</div>
      <span class="brand__tagline">India Restaurant</span>
    </div>
    <div class="mandala" role="img" aria-label="Circular floral mandala ornament in red, orange and gold"></div>
  </section>

  <section class="card card--back">
    <div class="brand">
      <div class="brand__name">velmorita</div>
      <span class="brand__tagline">India Restaurant</span>
    </div>
    <ul class="contact">
      <li class="contact__item">
        <span class="contact__label">Address:</span>
        <span class="contact__value">1840 Larkspur Avenue</span>
        <span class="contact__value">Fremont, CA94538</span>
      </li>
      <li class="contact__item">
        <span class="contact__label">Phone:</span>
        <span class="contact__value">408.555.0147</span>
      </li>
      <li class="contact__item">
        <span class="contact__label">Email:</span>
        <span class="contact__value">info@velmorita.com</span>
      </li>
      <li class="contact__item">
        <span class="contact__label">Web:</span>
        <span class="contact__value">www.velmorita.com</span>
      </li>
    </ul>
    <div class="mandala" role="img" aria-label="Partial floral mandala ornament rising from the lower edge of the card"></div>
  </section>
</body>
</html>
```